Flyer Design Project

We are a Human Resources and payroll company with a dedicated staffing and recruiting division. We need a really professional looking and creative flyer that breifly explains our offerings. This flyer will be given to other sales people that sell complementary services to what we offer. Those salespeople will to leave this flyer with prospective clients that want services that do not offer and we do.
Updates

I just uploades our logo in EPS!  Thank you!

Target Market(s)

Employers are our target market. Mostly healthcare but not exclusively.

Industry/Entity Type

It Company

Requirements
Must have
• Photos of people in a working environment would be good. All offering in attached files must be in the flyer as well as our logo.
Nice to have
• It would be nice to convey that we care about our clients and their employees.

```html
<!DOCTYPE html>
<html lang="en">
<head>
<meta charset="utf-8">
<title>HR Services Flyer</title>
<link href="https://fonts.googleapis.com/css2?family=Open+Sans:wght@400;700&display=swap" rel="stylesheet">
<style>
:root{
  --page:#ffffff;
  --orange-top:#f8a51c;
  --orange-bottom:#fbb338;
  --accent:#ef6a24;
  --ink:#231f1c;
  --white:#ffffff;
}
*{margin:0;padding:0;box-sizing:border-box}
html,body{width:849px;height:1200px;overflow:hidden;background:var(--page)}
body{font-family:"Open Sans",Arial,sans-serif;color:var(--ink)}
.flyer{position:relative;width:849px;height:1200px}
.panel{
  position:absolute;left:22px;top:22px;width:808px;height:1160px;
  border-radius:12px;
  background:linear-gradient(180deg,var(--orange-top),var(--orange-bottom));
  padding:14px 25px 0 21px;
}
.service{margin-bottom:15px}
.service h2,.package h3{
  font-size:14px;font-weight:700;letter-spacing:.4px;line-height:17px;
}
.service p,.package p,.package li{
  font-size:13.2px;line-height:15.7px;letter-spacing:.55px;text-align:justify;
}
.section-bar{
  display:inline-block;margin:-4px 0 12px -21px;
  background:var(--accent);color:var(--white);
  font-size:15px;font-weight:700;letter-spacing:.3px;
  padding:3px 30px 3px 23px;line-height:18px;
}
.package{margin-bottom:15px}
.package ul{list-style:none}
.package li{position:relative}
.package li::before{
  content:"";position:absolute;left:-17px;top:5px;width:9px;height:6px;background:var(--accent);
}
.package .note{padding-left:0}
.package ul + p{margin-top:0}
</style>
</head>
<body>
<div class="flyer">
  <div class="panel">
    <section class="service">
      <h2>New Hire On-Boarding</h2>
      <p>Improve productivity, build loyalty, and increase employee success by creating a positive first impression through an effective and efficient on-boarding process.</p>
    </section>
    <section class="service">
      <h2>Workers Compensation Analysis, Plan Design &amp; Claims Management</h2>
      <p>Working with you we will locate the lowest possible rates for your workers compensation insurance needs. We will manage the process with your vendor when injuries occur on the job.</p>
    </section>
    <section class="service">
      <h2>Unemployment Claims Administration</h2>
      <p>Many organizations do not realize that their unemployment rate is one area where cost savings can be realized. Through a combination of policy development, employee disciplinary procedures, and a cooperative partnership with the state Unemployment agency we can help to maintain or reduce your unemployment costs.</p>
    </section>
    <section class="service">
      <h2>Regulatory Compliance</h2>
      <p>Building off of the HR Audit and Risk Assessment our team will work with you to ensure that you are compliant in federal and state regulatory compliance.</p>
    </section>
    <section class="service">
      <h2>Payroll Administration &amp; Management</h2>
      <p>The service removes the worry of payroll and payroll taxes. Direct Deposit makes paying employees both quick and convenient.</p>
    </section>
    <section class="service">
      <h2>OSHA Program Development, Training &amp; Compliance</h2>
      <p>The Occupational Safety &amp; Health Administration regulates and enforces federally enacted safety standards for all different types of industries. The healthcare industry has some very specific requirements. We can work with you and your employees to ensure a safe and compliant working environment. This service will include the initial hazard assessment, preparation of your OSHA manual and monthly trainings.</p>
    </section>
    <section class="service">
      <h2>Recruitment &amp; Pre-Employment Services</h2>
      <p>Hiring the wrong person costs organizations valuable time and money. By developing and consistently following sound recruitment and pre-employment practices companies find that they are better able to manage their turnover. Our recruitment and pre-employment services include sourcing and prescreening candidates. In partnership with our background investigation organization we will thoroughly screen and advise clients in the hiring process.</p>
    </section>

    <div class="section-bar">Recruiting and Staffing Packages</div>

    <section class="package">
      <h3>Package A $275.00</h3>
      <ul>
        <li>Source up to 6 resumes</li>
        <li>Position is advertised on 1 job board</li>
      </ul>
      <p class="note">Note: Job Description is provided by client. &nbsp;We can provide this service to you for an additional fee of $35)</p>
    </section>
    <section class="package">
      <h3>Package B $ 390.00</h3>
      <ul>
        <li>Source up to 8 resumes</li>
        <li>Position advertised on 2 job boards</li>
        <li>Phone screen prospective candidates utilizing position specific requirements and questions provided by Client</li>
        <li>Client will be presented &nbsp;with a summarization of phone screen along with prospective candidates resume</li>
      </ul>
      <p class="note"><strong>Note:</strong> Job Description is provided by client. &nbsp;We can provide this service to you for an additional fee of $35)</p>
    </section>
    <section class="package">
      <h3>Package C $ 625.00</h3>
      <ul>
        <li>Source up to 10 resumes</li>
        <li>Create a customized job description that best fits your organizations needs</li>
        <li>Position advertised on 3 job boards</li>
        <li>Phone screen prospective candidates and conduct up to 3 in-person interviews based on position specific requirements</li>
        <li>Client will be presented with a summarization of the interviews, based on a candidate ranking system, &nbsp;as well as the prospective candidates resume</li>
      </ul>
    </section>
    <section class="package">
      <h3>Package D Percentage of Prospective Candidates Annual Salary</h3>
      <p>Recruiter will take the time to learn about your organization so they can identify individuals with qualities that will best match with your team. &nbsp;They will source, conduct in-depth interviews via phone and in-person, as well as perform thorough background and reference checks prior to employment.</p>
    </section>
    <section class="package">
      <h3>Package also included:</h3>
      <ul>
        <li>Create a customized job description that best fits your organizations needs</li>
        <li>Position advertised on 3 job boards</li>
        <li>Client will be presented with a summarization of the interviews, based on a candidate ranking system, &nbsp;as well as the prospective candidates resume</li>
      </ul>
    </section>
  </div>
</div>
</body>
</html>
```